Mortgage broker company need a attractive flyer design

We need a flyer design for our company based in Sydney called Bright Harbour Lending. Our perspective for this flyer is use our promotion to increase our customer bases. Our current promotion is : " If any new or existing customer do a mortgage consulting with us, customer can get a free consulting, a free customized property report ( $75 of value) and a free phone recharger ($50 of value and picture will be uploaded)." (wording can be rearranged, just give a idea of this promotion)
Our goal is to help our customer to achieve their financial targets, use our professionalism to well organize mortgage loans.
We are the mortgage broker, which can provide you over 30 financial institution's mortgage products. We make your comparison easier.b
our company details is uploaded.
To make this flyer more interesting, you can rearrange any wording and any picture.
Our website is www.brightharbourlending.com.au

Industry/Entity Type

Finance

```html
<!DOCTYPE html>
<html lang="en">
<head>
<meta charset="utf-8">
<title>Bright Harbour Lending – Flyer</title>
<link href="https://fonts.googleapis.com/css2?family=Open+Sans:wght@400;600;700&family=Roboto+Condensed:wght@700&display=swap" rel="stylesheet">
<style>
  :root{
    --stage:#dcdcdc;
    --navy:#2b2a86;
    --purple:#3c3a8f;
    --orange:#f0ac2e;
    --heading-orange:#f0581f;
    --band-deep:#22359a;
    --band-glow:#1aa3e6;
    --ink:#1f1f1f;
    --white:#ffffff;
    --body-top:#ffffff;
    --body-bottom:#c9cacc;
  }
  *{box-sizing:border-box;margin:0;padding:0}
  html,body{width:1200px;height:1000px;overflow:hidden;background:var(--stage)}
  .flyer{
    position:absolute;left:260px;top:22px;width:682px;height:953px;
    background:var(--white);overflow:hidden;
    font-family:"Open Sans",sans-serif;color:var(--ink);
  }
  .top-rule{position:absolute;left:0;top:0;width:100%;height:4px;background:var(--orange)}
  .hero-art{
    position:absolute;left:30px;top:28px;width:250px;height:180px;
    background:radial-gradient(ellipse at 55% 50%,#f2f2f2 0%,#d9d9d9 55%,#ffffff 80%);
    border-radius:6px;
  }
  .brand-name{
    position:absolute;left:415px;top:109px;
    font-weight:700;font-size:15px;color:var(--navy);letter-spacing:.2px;
  }
  .tagline{position:absolute;left:280px;top:156px;line-height:16px}
  .tagline .lead{font-weight:700;font-size:15px;color:var(--orange);line-height:20px}
  .tagline .sub{font-weight:600;font-size:12px;color:var(--navy)}
  .header-rule{position:absolute;left:0;top:214px;width:100%;height:4px;background:var(--purple)}
  .offer-band{
    position:absolute;left:0;top:226px;width:100%;height:202px;
    background:radial-gradient(ellipse 260px 120px at 52% 45%,var(--band-glow) 0%,#1d6fcc 40%,var(--band-deep) 100%);
    color:var(--white);font-family:"Roboto Condensed",sans-serif;font-weight:700;
    padding:14px 0 0 23px;
  }
  .offer-band h2{font-size:28px;line-height:35px;font-weight:700}
  .offer-band ul{list-style:none;margin-top:6px}
  .offer-band li{font-size:22px;line-height:30px;padding-left:19px;position:relative}
  .offer-band li::before{content:"";position:absolute;left:0;top:11px;width:10px;height:10px;border-radius:50%;background:var(--white)}
  .info{
    position:absolute;left:0;top:428px;width:100%;height:525px;
    background:radial-gradient(ellipse 420px 220px at 35% 10%,var(--body-top) 0%,#e6e7e8 55%,var(--body-bottom) 100%);
    padding:10px 29px 0 25px;
  }
  .info h3{font-size:20px;font-weight:700;color:var(--heading-orange);line-height:26px;margin-bottom:2px}
  .info h3.spaced{margin-top:7px;margin-bottom:4px}
  .info p{font-size:14.5px;line-height:20.5px;text-align:justify;margin-bottom:18.5px}
  .info p.intro{margin-bottom:0}
  .info strong{font-weight:600;color:var(--navy)}
  .info .brand{font-weight:700;color:var(--navy)}
</style>
</head>
<body>
<main class="flyer">
  <div class="top-rule"></div>
  <div class="hero-art" role="img" aria-label="Illustration of a figure pushing a shopping trolley carrying a small house"></div>
  <div class="brand-name">BRIGHT HARBOUR LENDING</div>
  <div class="tagline">
    <div class="lead">We make your comparison easier</div>
    <div class="sub">We are the mortgage broker, which</div>
    <div class="sub">can provide you over 30 financial institution's mortgage products.</div>
  </div>
  <div class="header-rule"></div>

  <section class="offer-band">
    <h2>If any new or existing customer<br>do a mortgage consulting with us &amp; customer can get</h2>
    <ul>
      <li>A free consulting</li>
      <li>A free phone recharger ($50 of value)</li>
      <li>A free customized property report ( $75 of value)</li>
    </ul>
  </section>

  <section class="info">
    <h3>ABOUT US</h3>
    <p class="intro"><span class="brand">BRIGHT HARBOUR LENDING</span> is aiming to find the right direction of your financial needs. We are your friend try to help you plan your financial needs, in the best way to achieve your financial needs for life. We will not only help you save huge amount of your money on interest rates, we will also plan you the right direction for you to receive investment benefit.</p>
    <h3 class="spaced">THE BEST ABOUT US</h3>
    <p><strong>We are specialised in mortgage industry</strong>, and our growing team is eager to help our clients. We will also look after each clients’ case identically, as we are always seeking the right direction for your financial goals.</p>
    <p><strong>For your convenience, we will book your appointment</strong> and come to you. All you need to do is call (02) 8100 4172 or 0412 55 3190, and book you in for your appointment at any time, even lunch break.</p>
    <p><strong>We will never push our clients to any unsuitable financial solutions</strong>, it is our ultimate goal to plan you a right financial way for life.</p>
    <p><strong>We are also partners of more than 10 different banks,</strong> as we can provide you big amount of alternative products for you to choose.</p>
    <p><strong>We are also specialised in different loan products,</strong> eg. Commercial loans*, Business lease, SMSF loans, Car loans and etc.</p>
  </section>
</main>
</body>
</html>
```